Veltrano Equity Partners business cards

Our company name is VELTRANO EQUITY PARTNERS. We need a business card for a start up company located in Medellin Colombia. The company will also be shortly expanding to USA. We are a Biotech company responsible for funding regenerative medicine projects with an emphasis on stem cell treatment and regeneration clinics. This will be a global company so the final design should communicate world wide financing for the new generation of regenerative medicine.

Industry/Entity Type

Business

```html
<!DOCTYPE html>
<html lang="en">
<head>
<meta charset="utf-8">
<title>Veltrano Equity Partners – Business Card</title>
<link rel="stylesheet" href="https://fonts.googleapis.com/css2?family=Questrial&display=swap">
<style>
  :root {
    --stage: #ece6ee;
    --card-white: #ffffff;
    --band-purple: #8a0a78;
    --brand-purple: #6e0f68;
    --accent-magenta: #b41fa6;
    --accent-soft: #e6c4e0;
    --band-text: #fbe9f8;
    --card-shadow: rgba(60, 20, 60, 0.18);
  }
  * { margin: 0; padding: 0; box-sizing: border-box; }
  html, body {
    width: 1200px;
    height: 1000px;
    overflow: hidden;
    background: var(--stage);
    font-family: "Questrial", "Century Gothic", sans-serif;
  }
  .stage {
    width: 1200px;
    height: 1000px;
    display: flex;
    align-items: center;
    justify-content: center;
  }
  .business-card {
    position: relative;
    width: 900px;
    height: 500px;
    background: var(--card-white);
    box-shadow: 0 12px 40px var(--card-shadow);
    overflow: hidden;
  }
  .brand-name {
    position: absolute;
    top: 58px;
    left: 60px;
    font-size: 38px;
    letter-spacing: 1px;
    color: var(--brand-purple);
  }
  .contact-band {
    position: absolute;
    left: 0;
    top: 180px;
    width: 100%;
    height: 200px;
    background: var(--band-purple);
    color: var(--band-text);
    padding: 22px 60px;
  }
  .holder-name {
    font-size: 30px;
    line-height: 1.1;
  }
  .holder-role {
    font-size: 22px;
    margin-bottom: 14px;
  }
  .contact-list {
    list-style: none;
    font-size: 19px;
    line-height: 1.3;
  }
  .contact-label {
    display: inline-block;
    width: 26px;
  }
  .decor-area {
    position: absolute;
    left: 520px;
    top: 110px;
    width: 320px;
    height: 360px;
    border-radius: 50%;
    background: radial-gradient(ellipse at center,
      rgba(180, 31, 166, 0.55) 0%,
      rgba(180, 31, 166, 0.25) 45%,
      rgba(230, 196, 224, 0) 72%);
  }
</style>
</head>
<body>
<main class="stage">
  <article class="business-card">
    <div class="brand-name">VELTRANO EQUITY PARTNERS</div>
    <section class="contact-band">
      <div class="holder-name">Sample Name</div>
      <div class="holder-role">CEO &amp; Founder</div>
      <ul class="contact-list">
        <li><span class="contact-label">m</span>+44 (0)123 456 7890</li>
        <li><span class="contact-label">t</span>+44 (0)123 456 7890</li>
        <li><span class="contact-label">e</span>sample.name@veltrano.eu</li>
        <li><span class="contact-label">w</span>www.veltrano-equity.com</li>
      </ul>
    </section>
    <div class="decor-area" role="img" aria-label="Large decorative brand graphic area"></div>
  </article>
</main>
</body>
</html>
```